Poly Gel bottle Design that stands out for Nail Company

I need a label design for the poly gel polish bottle. We are looking for a design that fit our brand store color and a clean design similar to our competitor.

We have 3 bottle Title: Gel Top Coat, Gel base Coat, Gel Matte Coat
The bottle will be white.

Also I will need 1 label for the extension gel.

Bottle volume is 15ml/0.5 fl oz

Target Market(s)

beauty acrylic nail and poly gel nail

Industry/Entity Type

Nail

Font styles to use
Serif
Decorative

Colors
6c459b

Requirements
Must have
• store color scheme. www.plumcrestshop.com

```html
<!DOCTYPE html>
<html lang="en">
<head>
<meta charset="utf-8">
<title>plum crest – Poly Gel Labels</title>
<link rel="stylesheet" href="https://fonts.googleapis.com/css2?family=Josefin+Sans:wght@700&family=Quicksand:wght@500&family=Parisienne&family=Lato:wght@400&display=swap">
<style>
  :root {
    --canvas-bg: #ececec;
    --panel-white: #fbfbfb;
    --ink: #111111;
    --plum: #6c459b;
    --label-radius: 14px;
  }
  * { margin: 0; padding: 0; box-sizing: border-box; }
  html, body {
    width: 1200px;
    height: 855px;
    overflow: hidden;
    background: var(--canvas-bg);
  }
  .label-set {
    position: relative;
    width: 1200px;
    height: 855px;
  }
  .label {
    position: absolute;
    top: 265px;
    width: 300px;
    height: 324px;
    border-radius: var(--label-radius);
    overflow: hidden;
    box-shadow: 0 2px 10px rgba(0,0,0,0.12);
  }
  .label--top   { left: 100px; }
  .label--base  { left: 450px; }
  .label--matte { left: 800px; }

  .label__art {
    position: absolute;
    inset: 0;
  }
  .label__art--marble {
    background:
      radial-gradient(ellipse at 20% 30%, #ff2fa8 0%, transparent 45%),
      radial-gradient(ellipse at 80% 70%, #ffd11a 0%, transparent 45%),
      radial-gradient(ellipse at 70% 20%, #2fb4f0 0%, transparent 40%),
      linear-gradient(135deg, #2fb4f0, #ff2fa8 40%, #ffd11a 75%, #2fb4f0);
  }
  .label__art--leaf {
    background:
      radial-gradient(ellipse at 10% 60%, #7fbfa3 0%, transparent 50%),
      radial-gradient(ellipse at 85% 30%, #f0c49a 0%, transparent 50%),
      linear-gradient(160deg, #e9cfb5, #a9cdb2 45%, #f1d48a 80%, #e8c4a6);
  }
  .label__art--paint {
    background:
      radial-gradient(ellipse at 25% 90%, #2f8fc0 0%, transparent 40%),
      radial-gradient(ellipse at 90% 20%, #2f6b3a 0%, transparent 25%),
      radial-gradient(ellipse at 5% 25%, #3d7a40 0%, transparent 22%),
      linear-gradient(150deg, #f6dd6a, #f3e48a 50%, #f5d64c 80%, #f0e9b8);
  }

  .label__panel {
    position: absolute;
    top: 0;
    left: 34px;
    width: 238px;
    height: 262px;
    background: var(--panel-white);
    text-align: center;
  }
  .label__brand {
    position: absolute;
    top: 36px;
    left: 0;
    right: 0;
    font-family: "Josefin Sans", sans-serif;
    font-weight: 700;
    font-size: 36px;
    letter-spacing: -0.5px;
    color: var(--ink);
    line-height: 1;
  }
  .label__title {
    position: absolute;
    top: 96px;
    left: 0;
    right: 0;
    font-family: "Quicksand", sans-serif;
    font-weight: 500;
    font-size: 22px;
    color: var(--plum);
    line-height: 1;
  }
  .label__type {
    position: absolute;
    top: 156px;
    left: 0;
    right: 0;
    font-family: "Parisienne", cursive;
    font-size: 27px;
    color: var(--ink);
    line-height: 1;
  }
  .label__volume {
    position: absolute;
    top: 229px;
    left: 0;
    right: 0;
    font-family: "Lato", sans-serif;
    font-size: 14px;
    color: var(--ink);
    line-height: 1;
  }
</style>
</head>
<body>
<main class="label-set">

  <section class="label label--top">
    <div class="label__art label__art--marble" role="img" aria-label="Marbled fluid paint pattern in pink, cyan and yellow"></div>
    <div class="label__panel">
      <p class="label__brand">plum crest</p>
      <p class="label__title">Gel Top Coat</p>
      <p class="label__type">poly gel polish</p>
      <p class="label__volume">15ml/0.5 fl oz</p>
    </div>
  </section>

  <section class="label label--base">
    <div class="label__art label__art--leaf" role="img" aria-label="Translucent leaf skeleton texture in beige, mint green and amber"></div>
    <div class="label__panel">
      <p class="label__brand">plum crest</p>
      <p class="label__title">Gel base Coat</p>
      <p class="label__type">poly gel polish</p>
      <p class="label__volume">15ml/0.5 fl oz</p>
    </div>
  </section>

  <section class="label label--matte">
    <div class="label__art label__art--paint" role="img" aria-label="Impasto oil painting of yellow and white flowers with blue and green strokes"></div>
    <div class="label__panel">
      <p class="label__brand">plum crest</p>
      <p class="label__title">Gel Matte Coat</p>
      <p class="label__type">poly gel polish</p>
      <p class="label__volume">15ml/0.5 fl oz</p>
    </div>
  </section>

</main>
</body>
</html>
```